new letterhead/envelope/business card design for law firm

please see attached pdf of current letterhead, envelope and business card. I am also attaching my new logo that I would like to be used. basically, I am looking to refresh and simplify my letterhead/stationary and business card, keeping the following in mind:

overall, I am going for the following look:

-simple,
-modern,
-classy,
-professional

Target Market(s)

law firm clients

Industry/Entity Type

Law Firm

Contact Information for Business Card

see attachment

Font styles to use
Sans Serif

Requirements
Must have
• overall, I am going for the following look:
• -simple,
• -modern,
• -classy,
• -professional
Nice to have
• same as above
Should not have
• no serif fonts

```html
<!DOCTYPE html>
<html lang="en">
<head>
<meta charset="utf-8">
<title>Calder Law – Stationery</title>
<link rel="stylesheet" href="https://fonts.googleapis.com/css2?family=Montserrat:wght@500;600;700&family=Nunito+Sans:wght@400;600&display=swap">
<style>
  :root {
    --backdrop: #ebeceb;
    --paper: #ffffff;
    --navy: #0c2b50;
    --green: #4f8d3c;
    --edge: #d9dbd9;
    --fold: #e6e8e6;
  }
  * { margin: 0; padding: 0; box-sizing: border-box; }
  html, body { width: 1200px; height: 1200px; overflow: hidden; }
  body {
    background: var(--backdrop);
    position: relative;
    font-family: "Nunito Sans", sans-serif;
    color: var(--navy);
  }
  .envelope {
    position: absolute;
    left: 85px; top: 75px;
    width: 1030px; height: 660px;
    background: var(--paper);
    border-radius: 42px 42px 0 0;
    box-shadow: 0 1px 3px rgba(0,0,0,0.12);
  }
  .envelope-fold {
    position: absolute;
    left: 0; right: 0; top: 145px;
    height: 1px;
    background: var(--fold);
  }
  .brand {
    position: absolute;
    text-align: center;
    transform: translateX(-50%);
  }
  .brand-dot {
    display: block;
    margin: 0 auto;
    border-radius: 50%;
    background: var(--navy);
  }
  .brand-name {
    display: block;
    font-family: "Montserrat", sans-serif;
    font-weight: 600;
    color: var(--navy);
    white-space: nowrap;
    letter-spacing: 0.5px;
  }
  .envelope .brand { left: 123px; top: 193px; }
  .envelope .brand-dot { width: 88px; height: 88px; }
  .envelope .brand-name { font-size: 27px; margin-top: 12px; }
  .return-address {
    font-size: 12px;
    line-height: 15px;
    margin-top: 12px;
    font-weight: 600;
  }
  .card {
    position: absolute;
    top: 825px;
    width: 516px; height: 298px;
    background: var(--paper);
    box-shadow: 0 1px 3px rgba(0,0,0,0.12);
  }
  .card-left { left: 71px; }
  .card-right { left: 615px; }
  .card .brand { left: 137px; top: 77px; }
  .card .brand-dot { width: 96px; height: 96px; }
  .card .brand-name { font-size: 30px; margin-top: 14px; }
  .card-details {
    position: absolute;
    right: 33px; top: 34px;
    text-align: right;
    font-size: 14px;
    line-height: 17px;
  }
  .holder-name {
    font-family: "Montserrat", sans-serif;
    font-weight: 700;
    font-size: 14.5px;
    letter-spacing: 0.2px;
  }
  .holder-title { font-size: 15px; margin-top: 3px; }
  .contact-lines { margin-top: 65px; }
  .label { margin-right: 4px; }
  .card-address { margin-top: 13px; }
  .card-right .holder-title,
  .card-right .label { color: var(--green); }
</style>
</head>
<body>
  <section class="envelope">
    <div class="envelope-fold"></div>
    <div class="brand">
      <span class="brand-dot"></span>
      <span class="brand-name">CALDER LAW</span>
      <p class="return-address">2240 Harbor Lane, Suite 410<br>Raleigh, NC 27607</p>
    </div>
  </section>

  <section class="card card-left">
    <div class="brand">
      <span class="brand-dot"></span>
      <span class="brand-name">CALDER LAW</span>
    </div>
    <div class="card-details">
      <p class="holder-name">DANIEL R. CALDER, ESQ</p>
      <p class="holder-title">Licensed in NC and FL</p>
      <div class="contact-lines">
        <p><span class="label">PHONE</span>919-555-0142</p>
        <p><span class="label">FAX</span>919-555-0178</p>
        <p><span class="label">CELL</span>919-555-0190</p>
        <p>dan@calderlawpa.com</p>
        <p>www.calderlawpa.com</p>
      </div>
      <p class="card-address">2240 Harbor Lane, Suite 410<br>Raleigh, NC 27607</p>
    </div>
  </section>

  <section class="card card-right">
    <div class="brand">
      <span class="brand-dot"></span>
      <span class="brand-name">CALDER LAW</span>
    </div>
    <div class="card-details">
      <p class="holder-name">DANIEL R. CALDER, ESQ</p>
      <p class="holder-title">Licensed in NC and FL</p>
      <div class="contact-lines">
        <p><span class="label">PHONE</span>919-555-0142</p>
        <p><span class="label">FAX</span>919-555-0178</p>
        <p><span class="label">CELL</span>919-555-0190</p>
        <p>dan@calderlawpa.com</p>
        <p>www.calderlawpa.com</p>
      </div>
      <p class="card-address">2240 Harbor Lane, Suite 410<br>Raleigh, NC 27607</p>
    </div>
  </section>
</body>
</html>
```